Modern, professional flyer for a Painting & decorating company. I would like to include my lo...

I run a small painting and decorating company that covers central and North London areas. I have a small crew of 3 painters that are all very experienced and have been painting for a least 20 years. We pride ourselves on being very efficient, friendly and carrying out work at an affordable cost.
I would like to include the different tasks we can carry out such as; Interior and exterior painting, residential, comercial and industrial jobs. Wallpaper hanging/ removal, filling and plastering. I would like also to include that I am on Fixaroster and have a current rating of 9.77. I'm also on Trusted Folk where if needed they can go and visit to look at past work and ratings.
I would like to keep the general outlook of the flyer simplistic as too much wording in my opinion puts people off reading it.

Target Market(s)

Local residential houses, shops, businesses etc.

Industry/Entity Type

Painting And Decorating

Colors

Designer to choose colors to be used in the design.

Requirements
Must have
• Size A5 Double sided.
• Contact Details
• Mobile 07846 203958
• Email: brushloft@mailvane.com

```html
<!DOCTYPE html>
<html lang="en">
<head>
<meta charset="utf-8">
<title>Brushloft – Painting &amp; Decorating Flyer</title>
<link rel="stylesheet" href="https://fonts.googleapis.com/css2?family=Teko:wght@500&family=Arimo:wght@400&display=swap">
<style>
  :root{
    --orange:#f8ad3a;
    --ink:#2e2e2e;
    --white:#ffffff;
    --page:#e6e8ec;
    --tick:#4caf3a;
    --dark:#222428;
  }
  *{margin:0;padding:0;box-sizing:border-box}
  html,body{width:1200px;height:1200px;overflow:hidden;background:var(--page)}
  .flyer{position:absolute;left:181px;top:0;width:849px;height:1200px;background:var(--white);overflow:hidden;font-family:"Arimo",Arial,sans-serif;color:var(--ink)}
  .hero{position:absolute;left:0;top:0;width:849px;height:530px}
  .headline{position:absolute;left:22px;top:92px;width:849px;text-align:center;font-family:"Teko","Arial Narrow",sans-serif;font-weight:500;line-height:74px;font-size:78px;color:#f2f2f4;letter-spacing:1px}
  .headline .accent{color:var(--orange)}
  .brand{position:absolute;left:740px;top:48px;width:100px;text-align:center;color:var(--white);font-size:14px;letter-spacing:0.5px}
  .brand-mark{display:block;width:30px;height:30px;margin:0 auto 10px;background:var(--white)}
  .tag{position:absolute;left:0;background:var(--orange);color:var(--white);border-radius:0 16px 16px 0;display:flex;align-items:center;padding-left:6px;white-space:nowrap}
  .tag-services{top:469px;width:219px;height:56px;font-size:28px}
  .tag-why{top:754px;width:361px;height:57px;font-size:35px;padding-left:10px}
  .services{position:absolute;left:20px;top:544px;list-style:none;font-size:26px;white-space:nowrap}
  .services li{height:44px;display:flex;align-items:center;gap:14px}
  .reasons{position:absolute;left:4px;top:834px;font-size:26px;line-height:30px;white-space:nowrap}
  .reason{display:flex;align-items:center;gap:12px;margin-bottom:8px}
  .reason svg{flex:none}
  .rating-line{position:absolute;left:0;top:950px;width:410px;text-align:center;font-size:26px;line-height:37px}
  .badge{position:absolute;left:20px;top:1028px;width:320px;height:82px}
  .badge svg{position:absolute;left:0;top:0}
  .badge-score{position:absolute;left:30px;top:10px;width:70px;text-align:center;font-family:"Teko","Arial Narrow",sans-serif;font-weight:500;font-size:52px;line-height:70px;color:var(--white)}
  .badge-name{position:absolute;left:100px;top:12px;width:200px;height:58px;line-height:58px;text-align:center;font-size:26px;color:var(--white)}
  .photo{position:absolute;border-radius:34px;border-bottom:8px solid var(--orange);overflow:hidden}
  .photo-front{left:463px;top:570px;width:355px;height:200px;background:linear-gradient(180deg,#4a4542,#3a3634 60%,#d9d9d6 62%,#3a3634 80%)}
  .photo-lounge{left:466px;top:838px;width:356px;height:200px;background:linear-gradient(90deg,#c9b46a 0%,#e9e9ec 28%,#5a2f87 55%,#e3e3e6 78%,#2a2c30 100%)}
  .contact{position:absolute;left:55px;top:1126px;width:738px;height:90px;background:var(--orange);border-radius:40px 40px 0 0;color:var(--white)}
  .contact-item{position:absolute;top:22px;display:flex;align-items:center;gap:10px;white-space:nowrap;line-height:40px}
  .contact-phone{left:24px;font-size:32px}
  .contact-email{left:320px;font-size:31px}
</style>
</head>
<body>
<main class="flyer">
  <svg class="hero" viewBox="0 0 849 530" width="849" height="530">
    <defs>
      <linearGradient id="heroTone" x1="0" y1="0" x2="1" y2="1">
        <stop offset="0" stop-color="#8e8fb4"/>
        <stop offset="0.45" stop-color="#6d6fa6"/>
        <stop offset="1" stop-color="#a9c9e6"/>
      </linearGradient>
    </defs>
    <rect role="img" aria-label="Softly blurred photo of a freshly painted living room with a purple feature wall" width="849" height="530" fill="url(#heroTone)"/>
    <path d="M0 416 C120 372 270 362 420 440 C560 512 720 532 849 440 V530 H0 Z" fill="#ffffff"/>
    <path d="M0 352 C120 318 300 330 440 446 C300 372 140 368 0 416 Z" fill="#f8ad3a"/>
  </svg>

  <h1 class="headline">HIGH QUALITY<br><span class="accent">PAINTING &amp; DECORATING</span><br>SERVICES</h1>

  <div class="brand"><span class="brand-mark"></span>BRUSHLOFT</div>

  <div class="tag tag-services">OUR SERVICES</div>
  <ul class="services">
    <li><svg width="24" height="28" viewBox="0 0 24 28"><path d="M2 16 L9 26 L22 2" fill="none" stroke="#4caf3a" stroke-width="3"/></svg>Interior and exterior painting</li>
    <li><svg width="24" height="28" viewBox="0 0 24 28"><path d="M2 16 L9 26 L22 2" fill="none" stroke="#4caf3a" stroke-width="3"/></svg>comercial and industrial jobs</li>
    <li><svg width="24" height="28" viewBox="0 0 24 28"><path d="M2 16 L9 26 L22 2" fill="none" stroke="#4caf3a" stroke-width="3"/></svg>Wallpaper hanging and removal</li>
    <li><svg width="24" height="28" viewBox="0 0 24 28"><path d="M2 16 L9 26 L22 2" fill="none" stroke="#4caf3a" stroke-width="3"/></svg>filling and plastering</li>
  </ul>

  <div class="photo photo-front" role="img" aria-label="Photo of a dark grey painted room with shuttered bay window and chandelier"></div>
  <div class="photo photo-lounge" role="img" aria-label="Photo of a bright lounge with a purple feature wall, sofa and large artwork"></div>

  <div class="tag tag-why">WHY CHOOSE US ?</div>
  <div class="reasons">
    <div class="reason">
      <svg width="40" height="30" viewBox="0 0 40 30"><circle cx="20" cy="8" r="5" fill="none" stroke="#2e2e2e" stroke-width="2"/><path d="M6 22 L10 18 L14 22 M16 26 L20 21 L24 26 M26 22 L30 18 L34 22" fill="none" stroke="#2e2e2e" stroke-width="2"/></svg>
      <span>more than 20 years experience</span>
    </div>
    <div class="reason">
      <svg width="40" height="30" viewBox="0 0 40 30"><path d="M2 10 L12 6 L22 12 L30 8 L38 12 L30 24 L24 28 L14 22 L4 18 Z" fill="#2e2e2e"/></svg>
      <span>friendly and respectful towards<br>customer privacy .</span>
    </div>
  </div>
  <p class="rating-line">97% of clients rate our service<br>as 'EXCELLENT'</p>

  <div class="badge">
    <svg width="320" height="82" viewBox="0 0 320 82" aria-hidden="true">
      <polygon points="30,0 120,0 90,82 0,82" fill="#f8ad3a"/>
      <polygon points="108,12 315,12 295,70 88,70" fill="#222428"/>
    </svg>
    <span class="badge-score">9.77</span>
    <span class="badge-name">Fixaroster</span>
  </div>

  <footer class="contact">
    <div class="contact-item contact-phone">
      <svg width="28" height="32" viewBox="0 0 28 32"><path d="M6 2 L12 2 L14 10 L10 13 C12 19 15 22 19 24 L22 20 L28 23 L27 30 C14 30 2 19 2 6 Z" fill="#ffffff"/></svg>
      <span>07846 203958</span>
    </div>
    <div class="contact-item contact-email">
      <svg width="40" height="34" viewBox="0 0 40 34"><rect x="2" y="10" width="36" height="22" fill="none" stroke="#ffffff" stroke-width="2"/><path d="M2 10 L20 24 L38 10" fill="none" stroke="#ffffff" stroke-width="2"/><circle cx="20" cy="8" r="6" fill="none" stroke="#ffffff" stroke-width="2"/></svg>
      <span>brushloft@mailvane.com</span>
    </div>
  </footer>
</main>
</body>
</html>
```